The Tideway- All Natural Company Needs Packaging for Main Product

Aloha!

We are a natural products company from Kaua’i, Hawaii called “The Tideway”

The first thing we need packaging for is for our all natural bug spray called “Natural Pest Ward”

We will need much more packaging for many other products in the future so we need a packaging design theme that will serve many products. Our other products are a Reef Safe Sunblock Face Stick called Cheek Shield
Reef Safe Sunblock Body Lotion called Skin Shield and other future natural products.

Very Important:
We love all Sol Pup packaging for its simplicity and cleanness. We honestly want our packaging to be just like Sol Pup in its own way. Instead of having the monkey, we want our Tideway logo to go in the middle like the monkey is on all Sol Pup packaging. We want everything else pretty much the same but just for Bug Spray. Though, we do not want to copy of course, but we would like it be similar.

Front Label- Needs to be on there: (Following guide of Sol Pup Front label)
1. Black Background
2. Tideway logo
3. Make it look professional
4. Make it Clean
5. Make it pop on the shelf
6. Needs to say the following:

** Please not we changed the brief. We changed it so Natural Pest Ward all goes together on the front as one logo for
Natural
Bug
Tideway

a. Natural Pest Ward (where Sol Pup is)
b. Tideway Logo (where monkey is)
c. Deet-Free. (where Golden Blend is)
d. Bug Spray (in between 2 lines) (where Tress Brightener is)
e. Natural Bug Spray enriched (where it says Premium Hair enriched…)
with quality essential oils that
repels mosquitos, gnats, no seeums,
ticks and all other bitey things.
f. Made with Aloha (where it says Blonde to Medium Brown Hair Types)
g. 4 FL OZ/ 118 mL (under Blonde to Medium Brown Hair Types)

Back Label-Things need on there: (Following guide of Sol Pup Back Label)

1. We have given an example Sol Pup Back Label. We would like it to look very similar to it.
2. Make room for a small UPC code on back.
3. Needs to say:

The Tideway products are naturally made for those to enjoy the outdoors.

Reef Safe Gluten Free Hypoallergenic Non-GMO
Deet Free Paraben Free Gluten Free Organic Ingredients

Product Description

Pest Ward is naturally enriched with quality essential oils to repel mosquitos, gnats, no seeums, ticks, and all other bites things. It is safe for babies, kids, and adults.

How to Use

Shake well and spray well on all parts of the body. Reapply every hour while outside.

Warning

Do not spray near or in eyes. If mistakenly sprayed in eyes, rinse with running water for 30 minutes.

Ingredients

Active Ingredients: Cedar wood oil (.35%) Citronella Oil (.30%) Eucalyptus Oil (.20%) Lemongrass Oil (.20%) Lavender Oil (.20%)
Inert Ingredients: Distilled Water, Coconut Oil, Witch Hazel

Exclusively Manufactured and Distributed by The Tideway LLC, 2836 Manuwela Ave. Kilauea, Hawaii, 96812 USA © All Rights Reserved
Get more information at examplepestward.test

Other Notes.
1. The label we’ve been using is 4”x5”
2. The Font we've been using for the Pest Ward logo part is Neutraface but we are glad to try other things that would make it look clean and stand out. Love the Sol Pup logo and font but definitely want something unique for us.

Thank you for all your hard work on this project. Please let us know if you have any questions, and we look forward to seeing your amazing packaging design.

Thanks and Aloha!
The Tideway Team

Target Market(s)

Retail Stores, Adventure Tours, Families

Industry/Entity Type

It Company

Font styles to use
Other font styles liked:
• Professional looking font

Colors
e34196
fbed22
00a990
000000
fbfbfb

Requirements
Must have
• Wrote everything above.
• Must Be VERY professional.
• Clean look.
• POP on a shelf.
• Creative
• White lettering to make it look clean with black background.
Nice to have
• Wrote everything above.
• Must be VERY professional.
• Clean look
• POP on a shelf
• Creative
Should not have
• Clutter
• not look professional
• distractions

```html
<!DOCTYPE html>
<html lang="en">
<head>
<meta charset="utf-8">
<title>Natural Pest Ward – Front Label</title>
<link href="https://fonts.googleapis.com/css2?family=Montserrat:wght@500;600;700&family=Allura&display=swap" rel="stylesheet">
<style>
  :root {
    --pink: #e34196;
    --yellow: #fbed22;
    --black: #000000;
    --white: #fbfbfb;
    --stage: #eeeeee;
  }
  * { margin: 0; padding: 0; box-sizing: border-box; }
  html, body {
    width: 1200px;
    height: 1200px;
    overflow: hidden;
    background: var(--stage);
  }
  .front-label {
    position: absolute;
    left: 200px;
    top: 100px;
    width: 800px;
    height: 1000px;
    background: var(--black);
    color: var(--white);
    font-family: "Montserrat", Arial, sans-serif;
    display: flex;
    flex-direction: column;
    align-items: center;
    padding-top: 56px;
    text-align: center;
  }
  .tagline {
    font-family: "Allura", cursive;
    font-size: 44px;
    line-height: 1;
    color: var(--white);
  }
  .brand {
    margin-top: 34px;
    display: flex;
    flex-direction: column;
    align-items: center;
  }
  .brand-square {
    width: 120px;
    height: 120px;
    background: var(--yellow);
  }
  .brand-name {
    margin-top: 26px;
    font-weight: 700;
    font-size: 62px;
    line-height: 1.05;
    color: var(--pink);
    text-transform: uppercase;
    letter-spacing: 1px;
  }
  .repels {
    margin-top: 34px;
    font-weight: 600;
    font-size: 40px;
    letter-spacing: 1px;
    padding: 14px 18px;
    border-top: 3px solid var(--white);
    border-bottom: 3px solid var(--white);
  }
  .pest-list {
    list-style: none;
    margin-top: 26px;
    font-weight: 500;
    font-size: 27px;
    line-height: 46px;
  }
  .deet-badge {
    margin-top: 24px;
    width: 128px;
    height: 128px;
    border: 3px solid var(--yellow);
    border-radius: 50%;
    display: flex;
    align-items: center;
    justify-content: center;
    color: var(--yellow);
    font-weight: 600;
    font-size: 29px;
    line-height: 1;
  }
  .volume {
    margin-top: 24px;
    font-weight: 600;
    font-size: 24px;
  }
  .aloha {
    margin-top: 20px;
    font-weight: 600;
    font-size: 29px;
    letter-spacing: 1px;
  }
</style>
</head>
<body>
  <section class="front-label">
    <p class="tagline">All-Natural Organic</p>
    <div class="brand">
      <div class="brand-square"></div>
      <h1 class="brand-name">Natural<br>Pest Ward</h1>
    </div>
    <h2 class="repels">REPELS</h2>
    <ul class="pest-list">
      <li>MOSQUITOS</li>
      <li>NO SEEUMS</li>
      <li>BITEY THINGS</li>
      <li>GNATS</li>
      <li>TICKS</li>
    </ul>
    <div class="deet-badge">DEET<br>FREE</div>
    <p class="volume">4oz.</p>
    <p class="aloha">MADE WITH ALOHA</p>
  </section>
</body>
</html>
```